domestic violence campaign

To Whom It May Concern:

We are fully aware that domestic violence can enter anyone’s life at any given time. As women we are faced with many demands as mothers, daughters, wives, sisters, providers, and friends. We often lose ourselves and our confidence. Harbor of Hope (HOH) Transitional Center of Western New York has embarked on a whole new way of intervention and prevention. As a domestic violence survivor I have created a facility and ideals which will enforce a revolution of Domestic Violence victims. For many years, growing up in suburbs of Western New York, I have come to terms with this fight. Domestic Violence can be stopped and prevented. As a domestic violence victim myself, being in live-in facility, as well as six different domestic violence shelters throughout the state, I fled from my domestic violence abuse. Without those temporary facilities, all that comes to my mind is death. They helped me rebuild and save my life but something was missing – zero education, training programs, parenting classes, personal strengthening workshops, on site at all. Considering the limited amount of time (30-45 days in an average shelter) and lack of resources, I was in need of the tools needed to move me from being a victim to having a stable life.
Opening more doors in Western New York is essential with the surrounding agencies and shelters overwhelmed from assisting women of crisis. Many issues have risen, as a result, such as: over-crowding, long waiting lists, and zero educational training with an on-site teaching curriculum. A repeated vicious cycle – victims regressing and not progressing with over 4000 cases of domestic violence reported throughout Erie County. The opening Harbor of Hope (HOH) Transitional Center of Western New York will provide a 9-24 month live-in facility, along with educational and training programs on-site that will serve as important tools to domestic violence victims. These educational based facilities and services are well needed for Western New York. Our trained certified staff will provide endless help to domestic violence victim. They will feel safe as they rebuild their lives and take advantage of our educational curriculum that has been designed to increase awareness and provide steppingstones to move the victims into confident stable independent human beings. Our clients will receive complete educational training, state testing, parenting classes, as well as strengthening, coping, and developing skills here at our facility. Harbor of Hope (HOH) Transitional Center is asking for your support.
Sincerely,
Marlena Brooks
President and CEO/website hohtcq.example
Harbor of Hope (HOH) Transitional Center of WNY

Industry/Entity Type

Training

Requirements
Nice to have
• we have already created our T-shirt/we will like for our T-shirt to be the center of the campaign to T-shirt reads
V IOLENCE
O N
W OMEN
S TOPS the campaign is to raise money so we can open doors and save lives

```html
<!DOCTYPE html>
<html lang="en">
<head>
<meta charset="utf-8">
<title>Harbor of Hope – Domestic Violence Campaign</title>
<link rel="stylesheet" href="https://fonts.googleapis.com/css2?family=Roboto+Condensed:wght@300;400;700;800&family=Arimo:wght@400;500&display=swap">
<style>
  :root {
    --purple: #5b2a82;
    --ink: #333333;
    --page: #ffffff;
    --panel-center: #ffffff;
    --panel-edge: #e1e1e3;
  }
  * { margin: 0; padding: 0; box-sizing: border-box; }
  html, body {
    width: 1200px; height: 923px; overflow: hidden;
    background: var(--page);
  }
  .poster {
    position: relative; width: 1200px; height: 923px;
    font-family: "Roboto Condensed", "Arial Narrow", sans-serif;
    color: var(--ink);
  }
  .panel {
    position: absolute; left: 30px; top: 32px; width: 1138px; height: 858px;
    background: radial-gradient(ellipse 55% 60% at 52% 42%, var(--panel-center) 0%, var(--panel-edge) 100%);
  }
  .brand {
    position: absolute; left: 52px; top: 72px;
    display: flex; align-items: center; gap: 16px;
    font-family: "Arimo", Arial, sans-serif; font-weight: 500;
    color: var(--purple);
  }
  .brand-dot { width: 64px; height: 64px; border-radius: 50%; background: var(--purple); }
  .brand-name { line-height: 1.05; }
  .brand-name .line-main { display: block; font-size: 27px; }
  .brand-name .line-sub { display: block; font-size: 23px; }
  .brand-name .line-region { display: block; font-size: 13px; letter-spacing: 0.3px; margin-top: 3px; }

  .donate {
    position: absolute; right: 62px; top: 58px; text-align: right;
  }
  .donate-call {
    font-weight: 800; font-size: 60px; line-height: 0.88; color: var(--purple);
    letter-spacing: -0.5px;
  }
  .donate-url {
    font-family: "Arimo", Arial, sans-serif; font-size: 24px;
    color: var(--ink); margin-top: 14px; letter-spacing: 0.3px;
  }

  .message { position: absolute; left: 345px; top: 236px; width: 495px; }
  .message .row {
    display: block; width: 495px; font-size: 60px; line-height: 66px;
    text-align: justify; text-align-last: justify; white-space: nowrap;
    font-weight: 300; text-transform: uppercase;
  }
  .message .row.tight { letter-spacing: -1.5px; }
  .message .row.wide { letter-spacing: 3px; }
  .message strong { font-weight: 800; color: var(--purple); }
  .message .row.lead strong { letter-spacing: 0.5px; }
  .message .gap { height: 40px; }
  .message .row.end { text-align-last: left; }

  .pledge {
    position: absolute; left: 345px; top: 718px;
    font-family: "Arimo", Arial, sans-serif; font-size: 28px; line-height: 34px;
    letter-spacing: -0.5px; color: var(--ink);
  }
  .pledge .indent { padding-left: 16px; }
  .pledge em { font-style: normal; color: var(--purple); }

  .tagline {
    position: absolute; right: 57px; top: 848px;
    font-family: "Arimo", Arial, sans-serif; font-size: 26px; letter-spacing: 1.5px;
  }
  .tagline strong {
    font-family: "Roboto Condensed", sans-serif; font-weight: 800;
    color: var(--purple); letter-spacing: 0;
  }
</style>
</head>
<body>
<main class="poster">
  <div class="panel"></div>

  <header class="brand">
    <span class="brand-dot" aria-hidden="true"></span>
    <span class="brand-name">
      <span class="line-main">Harbor of Hope</span>
      <span class="line-sub">Transitional Center</span>
      <span class="line-region">WESTERN NEW YORK</span>
    </span>
  </header>

  <aside class="donate">
    <div class="donate-call">DONATE<br>TODAY!</div>
    <div class="donate-url">HOHTCQ.EXAMPLE</div>
  </aside>

  <section class="message">
    <span class="row lead"><strong>Domestic Violence</strong></span>
    <span class="row">Can enter anyone’s</span>
    <span class="row tight">Life at any given <strong>time.</strong></span>
    <div class="gap"></div>
    <span class="row">Domestic violence</span>
    <span class="row wide">Can be <strong>stopped</strong> or</span>
    <span class="row end"><strong>Prevented.</strong></span>
  </section>

  <p class="pledge">
    PLACE YOUR AD, AND SPEAK OUT:<br>
    <span class="indent">TAKE THE “<em>VOWS WITH HOH</em>.”</span>
  </p>

  <footer class="tagline">VIOLENCE ON WOMEN <strong>STOP NOW.</strong></footer>
</main>
</body>
</html>
```